buisness card

This project is linked to Harrowgate Freight.

Our company needs a Business Card Design. Please refer to our original project in the link above.

overview

```html
<!DOCTYPE html>
<html lang="en">
<head>
<meta charset="utf-8">
<title>Harrowgate Freight — Business Cards</title>
<link href="https://fonts.googleapis.com/css2?family=Montserrat:wght@400;700&display=swap" rel="stylesheet">
<style>
  :root {
    --page: #ececea;
    --card-light: #ffffff;
    --card-dark: #0d0c0c;
    --ink: #262626;
    --ink-soft: #4a4a4a;
    --rule: #5a5a5a;
    --on-dark: #ffffff;
    --shadow: 0 6px 14px rgba(0,0,0,0.28);
  }
  * { box-sizing: border-box; margin: 0; padding: 0; }
  html, body { width: 1128px; height: 1200px; overflow: hidden; }
  body {
    background: var(--page);
    font-family: "Montserrat", Arial, sans-serif;
    color: var(--ink);
    position: relative;
  }
  .card-set {
    position: absolute;
    left: 21px;
    display: flex;
    gap: 13px;
  }
  .card-set--ops { top: 81px; }
  .card-set--transfer { top: 448px; }
  .card-set--owner { top: 808px; }

  .card {
    position: relative;
    width: 536px;
    height: 302px;
    box-shadow: var(--shadow);
  }
  .card--front { background: var(--card-light); }
  .card--back {
    background: var(--card-dark);
    display: flex;
    align-items: center;
    justify-content: center;
  }

  .brand-name {
    font-weight: 400;
    letter-spacing: 0.2px;
    white-space: nowrap;
  }
  .card__brand {
    position: absolute;
    left: 24px;
    top: 178px;
    font-size: 19px;
    color: var(--ink);
  }
  .card--back .brand-name {
    font-size: 34px;
    color: var(--on-dark);
    margin-top: 58px;
  }

  .contact {
    position: absolute;
    left: 257px;
    width: 256px;
  }
  .contact__person { font-size: 19px; line-height: 1; color: var(--ink); }
  .contact__person b { font-weight: 700; }
  .contact__role {
    font-size: 12px;
    margin-top: 5px;
    letter-spacing: 0.2px;
    text-transform: uppercase;
  }
  .contact__role b { font-weight: 700; }
  .contact__company {
    font-size: 17px;
    color: var(--ink);
    padding-bottom: 2px;
    border-bottom: 1.5px solid var(--rule);
  }
  .contact__address {
    font-size: 13px;
    line-height: 18px;
    color: var(--ink-soft);
    margin-top: 8px;
  }
  .contact__lines { list-style: none; margin-top: 7px; }
  .contact__line {
    display: flex;
    align-items: center;
    gap: 10px;
    height: 31px;
    font-size: 13.5px;
    color: var(--ink-soft);
  }
  .contact__line svg { width: 19px; height: 19px; flex: none; fill: var(--ink); }

  .card-set--ops .contact--person { top: 50px; }
  .card-set--ops .contact--company { top: 133px; }
  .card-set--transfer .contact--person { top: 44px; }
  .card-set--transfer .contact--company { top: 146px; }
  .card-set--owner .contact--person { top: 40px; }
  .card-set--owner .contact--company { top: 121px; }
</style>
</head>
<body>

<svg width="0" height="0" style="position:absolute" aria-hidden="true">
  <defs>
    <symbol id="icon-mobile" viewBox="0 0 20 20"><path d="M6 1h8a1.5 1.5 0 0 1 1.5 1.5v15A1.5 1.5 0 0 1 14 19H6a1.5 1.5 0 0 1-1.5-1.5v-15A1.5 1.5 0 0 1 6 1zm.3 2.2v12.3h7.4V3.2zM10 16.3a.9.9 0 1 0 0 1.8.9.9 0 0 0 0-1.8z"/></symbol>
    <symbol id="icon-phone" viewBox="0 0 20 20"><path d="M1 7.5C1 4.5 5 3 10 3s9 1.5 9 4.5v1.2h-4.2V6.9c-1.4-.5-3-.7-4.8-.7s-3.4.2-4.8.7v1.8H1zM6 9.5h8l3.5 4.2V17H2.5v-3.3zm4 1.7a2.2 2.2 0 1 0 0 4.4 2.2 2.2 0 0 0 0-4.4z"/></symbol>
    <symbol id="icon-mail" viewBox="0 0 20 20"><path d="M1 4h18v1.6l-9 5.6-9-5.6zm0 3.6 9 5.6 9-5.6V16H1z"/></symbol>
  </defs>
</svg>

<section class="card-set card-set--ops">
  <article class="card card--front">
    <div class="card__brand brand-name">Harrowgate Freight</div>
    <div class="contact contact--person">
      <p class="contact__person">R. DALE <b>WHITAKER</b></p>
      <p class="contact__role"><b>Operations</b> Manager</p>
    </div>
    <div class="contact contact--company">
      <p class="contact__company brand-name">Harrowgate Freight</p>
      <p class="contact__address">415 Larkspur<br>Dr. Brennan, NC 27455</p>
      <ul class="contact__lines">
        <li class="contact__line"><svg><use href="#icon-mobile"/></svg>555 210 4861</li>
        <li class="contact__line"><svg><use href="#icon-phone"/></svg>555 318-2290</li>
        <li class="contact__line"><svg><use href="#icon-mail"/></svg>rdwhauling@mailbox.com</li>
      </ul>
    </div>
  </article>
  <article class="card card--back">
    <div class="brand-name">Harrowgate Freight</div>
  </article>
</section>

<section class="card-set card-set--transfer">
  <article class="card card--front">
    <div class="card__brand brand-name">Harrowgate Freight</div>
    <div class="contact contact--person">
      <p class="contact__person">MARCUS <b>HALE</b></p>
      <p class="contact__role"><b>Transfer</b> Department</p>
    </div>
    <div class="contact contact--company">
      <p class="contact__company brand-name">Harrowgate Freight</p>
      <p class="contact__address">415 Larkspur<br>Dr. Brennan, NC 27455</p>
      <ul class="contact__lines">
        <li class="contact__line"><svg><use href="#icon-mobile"/></svg>555 407 3318</li>
        <li class="contact__line"><svg><use href="#icon-phone"/></svg>555 318 2290</li>
      </ul>
    </div>
  </article>
  <article class="card card--back">
    <div class="brand-name">Harrowgate Freight</div>
  </article>
</section>

<section class="card-set card-set--owner">
  <article class="card card--front">
    <div class="card__brand brand-name">Harrowgate Freight</div>
    <div class="contact contact--person">
      <p class="contact__person">GLEN <b>WHITAKER</b></p>
      <p class="contact__role"><b>Owner</b></p>
    </div>
    <div class="contact contact--company">
      <p class="contact__company brand-name">Harrowgate Freight</p>
      <p class="contact__address">415 Larkspur<br>Dr. Brennan, NC 27455</p>
      <ul class="contact__lines">
        <li class="contact__line"><svg><use href="#icon-mobile"/></svg>555 629 0574</li>
        <li class="contact__line"><svg><use href="#icon-phone"/></svg>555 318 2290</li>
        <li class="contact__line"><svg><use href="#icon-mail"/></svg>gwhitaker@whitakergroup.com</li>
      </ul>
    </div>
  </article>
  <article class="card card--back">
    <div class="brand-name">Harrowgate Freight</div>
  </article>
</section>

</body>
</html>
```